Harbor Lane Web Design upgrade (hlwd-studio.net)

Need redesign of agency website using one-page WordPress theme (possibly Velmo theme, attached).

Requirements:
- use company logo
- flat design
- responsive
- modern Searchly fonts (e.g. - Gotham)
- in header
- logo
- phone (text) 615.482.7039
- cities (text) Boston, Hartford, Nashville
- top navigation bar
- portfolio needs 1 good image and descriptive text
(see Velmo portfolio templates)
- portfolio images will not link to live sites at this time
- working contact form

Target Market(s)

web and app development clients, online marketing consulting clients

Industry/Entity Type

It Company

Coding

Coded - Design and coding required

Font styles to use
Sans Serif
Other font styles liked:
• Gotham or other modern Searchly fonts

Requirements
Must have
• HLWD company logo (attached), flat design, responsive, modern Searchly fonts (like Gotham), WordPress (Velmo if possible, attached), phone number, cities served, portfolio, contact form with budget checkboxes.
Nice to have
• Designer can change logo colors if they feel strongly about a creative idea.
Should not have
• clip art, non royalty free images, nothing that looks like 1998.

```html
<!DOCTYPE html>
<html lang="en">
<head>
<meta charset="utf-8">
<title>Harbor Lane Web Design</title>
<link rel="stylesheet" href="https://fonts.googleapis.com/css2?family=Ubuntu:wght@400;500;700&family=Open+Sans:wght@400;600&family=Noto+Serif:wght@700&display=swap">
<style>
:root{
  --navy:#0f3d7d;
  --green:#2d6a45;
  --ink:#222;
  --muted:#777;
  --band:#f6f6f6;
  --white:#fff;
  --footer:#262626;
}
*{box-sizing:border-box;margin:0;padding:0}
html,body{width:1200px;height:2643px;overflow:hidden;background:var(--white)}
body{position:relative;font-family:"Open Sans",sans-serif;color:var(--ink)}
.abs{position:absolute}

/* header */
.site-header{position:absolute;left:0;top:0;width:1200px;height:106px;background:var(--white)}
.brand{position:absolute;left:97px;top:26px;font-family:"Ubuntu",sans-serif;font-weight:700;font-size:25px;line-height:27px;color:#111;width:200px}
.nav a{position:absolute;top:0;height:106px;line-height:106px;font-family:"Ubuntu",sans-serif;font-size:14px;color:#222;text-decoration:none}
.nav .active{left:566px;width:74px;background:var(--green);color:var(--white);text-align:center}
.search{position:absolute;left:1086px;top:45px}

/* hero */
.hero{position:absolute;left:0;top:106px;width:1200px;height:516px;background:linear-gradient(120deg,#cfd3d8 0%,#eef0f2 45%,#dfe2e6 100%)}
.hero-title{position:absolute;left:587px;top:346px;font-family:"Noto Serif",serif;font-size:31px;color:var(--navy)}
.hero-text{position:absolute;left:592px;top:392px;width:490px;font-size:12.5px;line-height:21px;color:#222}

/* welcome */
.section-title{position:absolute;left:0;width:1200px;text-align:center;font-family:"Ubuntu",sans-serif;font-weight:700;font-size:27px;color:var(--navy)}
.section-title .accent{color:var(--green)}
.welcome-text{position:absolute;left:174px;top:712px;width:852px;text-align:center;font-size:12.5px;line-height:22px;color:#333}
.btn{position:absolute;left:544px;top:823px;width:111px;height:44px;background:var(--navy);color:var(--white);border-radius:3px;font-family:"Ubuntu",sans-serif;font-size:15px;line-height:44px;text-align:center}

/* services */
.services{position:absolute;left:0;top:927px;width:1200px;height:465px;background:var(--band)}
.eyebrow{position:absolute;left:0;top:30px;width:1200px;text-align:center;font-family:"Ubuntu",sans-serif;font-size:17px;color:var(--green)}
.service{position:absolute;width:330px;height:110px}
.service svg{position:absolute;left:0;top:0}
.service h3{position:absolute;left:110px;top:0;width:200px;font-family:"Ubuntu",sans-serif;font-weight:500;font-size:16px;line-height:22px;color:#222}
.service p{position:absolute;left:110px;width:190px;font-size:12.5px;line-height:23px;color:var(--muted);text-align:justify}

/* portfolio */
.portfolio-grid{position:absolute;left:0;top:1515px;width:1200px;height:397px}
.tile{position:absolute;width:300px;height:198px}
.tile-hover{background:rgba(20,40,35,.82)}
.tile-hover .zoom{position:absolute;left:131px;top:12px}
.tile-hover h4{position:absolute;left:0;top:78px;width:300px;text-align:center;font-family:"Ubuntu",sans-serif;font-weight:500;font-size:16px;color:var(--white)}
.tile-hover p{position:absolute;left:25px;top:108px;width:250px;text-align:center;font-size:12.5px;line-height:21px;color:#eee}

/* testimonials */
.avatar{position:absolute;width:106px;height:106px;border-radius:50%;background:linear-gradient(160deg,#d8dde3,#8d98a6);border:4px solid #e8e8e8}
.quote{position:absolute;width:250px;font-size:12.5px;line-height:22px;color:#777;text-align:justify}
.who{position:absolute;font-family:"Ubuntu",sans-serif;font-weight:500;font-size:16px;color:#1d7fa8}
.role{position:absolute;font-size:12px;color:#999}
.arrow{position:absolute;width:38px;height:38px;border-radius:50%;background:#e6e6e6}

/* contact */
.map{position:absolute;left:0;top:2243px;width:1200px;height:354px;background:linear-gradient(135deg,#d6d9d0,#e8e6dd 50%,#cfd5cb)}
.map-tag{position:absolute;left:246px;top:2274px;padding:0 8px;height:24px;line-height:24px;background:var(--green);color:var(--white);font-size:12.5px}
.contact-box{position:absolute;left:396px;top:2352px;width:407px;height:136px;background:var(--green);color:var(--white);text-align:center}
.contact-box h2{margin-top:18px;font-family:"Ubuntu",sans-serif;font-weight:700;font-size:26px}
.contact-box .line{margin-top:12px;font-size:12.5px}
.contact-box .line svg{vertical-align:-2px;margin-right:6px}

.site-footer{position:absolute;left:0;top:2597px;width:1200px;height:46px;background:var(--footer);color:#ddd;font-size:11.5px}
.site-footer .copy{position:absolute;left:97px;top:15px}
.site-footer .follow{position:absolute;left:910px;top:15px}
.social{position:absolute;top:12px;width:21px;height:21px;border-radius:50%;border:1.5px solid #bbb}
</style>
</head>
<body>

<header class="site-header">
  <div class="brand">Harbor Lane<br>Web Design</div>
  <nav class="nav">
    <a class="active" href="#">Home</a>
    <a href="#" style="left:664px">Portfolio</a>
    <a href="#" style="left:756px">Client testimonials</a>
    <a href="#" style="left:903px">Services</a>
    <a href="#" style="left:993px">Contact us</a>
  </nav>
  <svg class="search" width="16" height="16" viewBox="0 0 16 16"><circle cx="6.5" cy="6.5" r="5" fill="none" stroke="#111" stroke-width="2.2"/><line x1="10" y1="10" x2="15" y2="15" stroke="#111" stroke-width="2.5"/></svg>
</header>

<section class="hero" role="img" aria-label="Photo of colleagues at a desk with a laptop and printed charts"></section>
<h1 class="hero-title">Website Design and Development</h1>
<p class="hero-text">A successful business needs the competitive edge a professionally designed website offers. At Harbor Lane Web Design we work with the customer to create a unique identity that is tailored to their individual needs and business goals.</p>

<h2 class="section-title" style="top:670px">WELCOME TO <span class="accent">HARBOR LANE</span></h2>
<p class="welcome-text">Stagnancy has really become a site killer. From 1998 - 2006, we were #1 for our top keys... and admittedly did very little to accomplish that. Of course we bragged on it no end. Now Searchly demands fresh, unique content and a few other attributes to be in place before they give up any precious rankings. It's amazing to see so many out-of-state design firms ranking for NASHVILLE WEBSITE DESIGN these days. The good news is that they are asleep at the wheel in most other major engines. If they want to hang their hats on the Searchly rack, so be it.</p>
<div class="btn">View More</div>

<section class="services">
  <div class="eyebrow">Our Services</div>
  <h2 class="section-title" style="top:66px">POWERFUL WEBSITES THAT LOOK BEAUTIFUL</h2>

  <div class="service" style="left:104px;top:130px">
    <svg width="120" height="120" viewBox="0 0 120 120"><circle cx="58" cy="57" r="57" fill="none" stroke="#2d6a45" stroke-width="2.5"/><circle cx="58" cy="57" r="48" fill="#2d6a45"/><rect x="38" y="42" width="40" height="27" fill="none" stroke="#fff" stroke-width="3"/><line x1="58" y1="69" x2="58" y2="76" stroke="#fff" stroke-width="3"/><line x1="48" y1="77" x2="68" y2="77" stroke="#fff" stroke-width="3"/><line x1="48" y1="62" x2="66" y2="48" stroke="#fff" stroke-width="2.5"/></svg>
    <h3 style="left:122px;top:-4px">Website Design and Development</h3>
    <p style="left:122px;top:41px">A successful business needs the competitive edge a professionally designed website offers.</p>
  </div>

  <div class="service" style="left:451px;top:141px">
    <svg width="94" height="94" viewBox="0 0 94 94"><circle cx="46" cy="46" r="46" fill="#0f3d7d"/><circle cx="46" cy="46" r="20" fill="none" stroke="#fff" stroke-width="3"/><circle cx="46" cy="46" r="9" fill="#fff"/></svg>
    <h3 style="left:109px;top:0">Logo Design</h3>
    <p style="left:109px;top:30px">A successful business needs the competitive edge a professionally designed website offers.</p>
  </div>

  <div class="service" style="left:784px;top:141px">
    <svg width="94" height="94" viewBox="0 0 94 94"><circle cx="46" cy="46" r="46" fill="#0f3d7d"/><path d="M27 34h7l6 20h22l5-15H37" fill="none" stroke="#fff" stroke-width="3"/><circle cx="43" cy="61" r="3" fill="#fff"/><circle cx="59" cy="61" r="3" fill="#fff"/></svg>
    <h3 style="left:110px;top:0">E-Commerce Solutions</h3>
    <p style="left:110px;top:30px">A successful business needs the competitive edge a professionally designed website offers.</p>
  </div>

  <div class="service" style="left:116px;top:312px">
    <svg width="94" height="94" viewBox="0 0 94 94"><circle cx="46" cy="46" r="46" fill="#0f3d7d"/><rect x="30" y="44" width="7" height="18" fill="#fff"/><rect x="40" y="34" width="7" height="28" fill="#fff"/><circle cx="55" cy="52" r="7" fill="none" stroke="#fff" stroke-width="3"/><line x1="60" y1="57" x2="66" y2="63" stroke="#fff" stroke-width="3"/></svg>
    <h3 style="left:110px;top:0">Advanced Marketing</h3>
    <p style="left:110px;top:30px">A successful business needs the competitive edge a professionally designed website offers.</p>
  </div>

  <div class="service" style="left:451px;top:312px">
    <svg width="94" height="94" viewBox="0 0 94 94"><circle cx="46" cy="46" r="46" fill="#0f3d7d"/><ellipse cx="44" cy="32" rx="14" ry="5" fill="#fff"/><path d="M30 36v8c0 3 6 5 14 5s14-2 14-5v-8c0 3-6 5-14 5s-14-2-14-5zM30 48v8c0 3 6 5 14 5 2 0 3 0 4 0v-6c-1 0-3 0-4 0-8 0-14-2-14-5z" fill="#fff"/><circle cx="57" cy="58" r="6" fill="none" stroke="#fff" stroke-width="3"/></svg>
    <h3 style="left:109px;top:0">Database Integration</h3>
    <p style="left:109px;top:30px">A successful business needs the competitive edge a professionally designed website offers.</p>
  </div>

  <div class="service" style="left:784px;top:312px">
    <svg width="94" height="94" viewBox="0 0 94 94"><circle cx="46" cy="46" r="46" fill="#0f3d7d"/><circle cx="38" cy="40" r="6" fill="#fff"/><path d="M27 60c0-8 5-12 11-12s11 4 11 12z" fill="#fff"/><circle cx="56" cy="34" r="6" fill="#fff"/><path d="M48 52c1-6 4-10 8-10 6 0 10 4 10 10z" fill="#fff"/></svg>
    <h3 style="left:110px;top:0">Consultation</h3>
    <p style="left:110px;top:30px">A successful business needs the competitive edge a professionally designed website offers.</p>
  </div>
</section>

<h2 class="section-title" style="top:1442px">OUR <span class="accent">PORTFOLIO</span></h2>
<div class="portfolio-grid">
  <div class="tile" style="left:0;top:0;background:linear-gradient(#b9cde0,#7a8a4e)" role="img" aria-label="Portfolio photo: group of people in a green field"></div>
  <div class="tile tile-hover" style="left:300px;top:0">
    <svg class="zoom" width="38" height="38" viewBox="0 0 38 38"><circle cx="19" cy="19" r="19" fill="#2d6a45"/><circle cx="17" cy="17" r="6" fill="none" stroke="#fff" stroke-width="2.5"/><line x1="21" y1="21" x2="26" y2="26" stroke="#fff" stroke-width="2.5"/></svg>
    <h4>SIGNAL DEPOT WAREHOUSE</h4>
    <p>At vero eos et accusamus et iusto odio dig-nissimos ducimus qui blanditiis praesentium voluptatum delenit...</p>
  </div>
  <div class="tile" style="left:600px;top:0;background:linear-gradient(#a7aaad,#5d6368)" role="img" aria-label="Portfolio photo: businessman with binoculars above a city"></div>
  <div class="tile" style="left:900px;top:0;background:linear-gradient(#c7c49a,#7c8256)" role="img" aria-label="Portfolio photo: wedding shoes on grass"></div>
  <div class="tile" style="left:0;top:198px;background:linear-gradient(#e0a53a,#4e6b22)" role="img" aria-label="Portfolio photo: vineyard rows at sunset"></div>
  <div class="tile" style="left:300px;top:198px;background:linear-gradient(#b7c4cc,#78828a)" role="img" aria-label="Portfolio photo: person holding a sketch of an idea"></div>
  <div class="tile" style="left:600px;top:198px;background:linear-gradient(#e9e3da,#b9a99a)" role="img" aria-label="Portfolio photo: hands with a tablet and coffee"></div>
  <div class="tile" style="left:900px;top:198px;background:linear-gradient(#dbe4ee,#7b8ea6)" role="img" aria-label="Portfolio photo: tablet showing charts on a desk"></div>
</div>

<h2 class="section-title" style="top:1956px">CLIENT <span class="accent">TESTIMONIALS</span></h2>
<div class="avatar" style="left:165px;top:2019px" role="img" aria-label="Client portrait"></div>
<p class="quote" style="left:303px;top:2018px">Lorem Ipsum is simply dummy text of the printing and typesetting industry. Lorem Ipsum has been the industry's standard dummy text ever since the 1500s,</p>
<div class="who" style="left:303px;top:2114px">Dana Whitfield,</div>
<div class="role" style="left:303px;top:2140px">Financial Services Professional</div>

<div class="avatar" style="left:647px;top:2019px" role="img" aria-label="Client portrait"></div>
<p class="quote" style="left:784px;top:2018px">Lorem Ipsum is simply dummy text of the printing and typesetting industry. Lorem Ipsum has been the industry's standard dummy text ever since the 1500s,</p>
<div class="who" style="left:784px;top:2114px">Marisol T. Okafor,</div>
<div class="role" style="left:784px;top:2140px">Financial Services Professional</div>

<div class="arrow" style="left:541px;top:2171px"><svg width="38" height="38" viewBox="0 0 38 38"><path d="M21 12l-7 7 7 7" fill="none" stroke="#fff" stroke-width="2.5"/></svg></div>
<div class="arrow" style="left:591px;top:2171px"><svg width="38" height="38" viewBox="0 0 38 38"><path d="M17 12l7 7-7 7" fill="none" stroke="#fff" stroke-width="2.5"/></svg></div>

<div class="map" role="img" aria-label="Street map of the service area"></div>
<div class="map-tag">Lorem Ipsum</div>
<div class="contact-box">
  <h2>Contact us</h2>
  <div class="line">
    <svg width="11" height="11" viewBox="0 0 12 12"><path d="M2 1l3 1 0 3-1.5 1c1 2 2 3 3.5 3.5L8 8l3 .5 0 2.5c-5 1-10-4-9-10z" fill="#fff"/></svg>PHONE : 615.482.7039, &nbsp;&nbsp;
    <svg width="8" height="12" viewBox="0 0 8 12"><rect x="1" y="0.5" width="6" height="11" rx="1" fill="none" stroke="#fff" stroke-width="1.4"/></svg>Unknown : 615.482.7039
  </div>
  <div class="line">
    <svg width="9" height="12" viewBox="0 0 10 14"><path d="M5 0a5 5 0 0 1 5 5c0 4-5 9-5 9S0 9 0 5a5 5 0 0 1 5-5z" fill="#fff"/><circle cx="5" cy="5" r="2" fill="#2d6a45"/></svg>Boston, Hartford, Nashville
  </div>
</div>

<footer class="site-footer">
  <div class="copy">© 2016 HarborLaneWebDesign. &nbsp;All Rights Reserved</div>
  <div class="follow">Follow us on</div>
  <span class="social" style="left:984px"></span>
  <span class="social" style="left:1009px"></span>
  <span class="social" style="left:1034px"></span>
  <span class="social" style="left:1059px"></span>
  <span class="social" style="left:1084px"></span>
</footer>

</body>
</html>
```